Labour Day banner showcasing 20% off site

Banner graphic promoting our Labour Day sale
Size: 2000px x 600px
- examples from other companies and their sale banners have been uploaded for inspiration. Labour day examples are for the United States's holiday and submissions should NOT be in their country colours.
- product images can be found at www.fernlowleaf.com

Target Market(s)

19+

Industry/Entity Type

Cannabis

Requirements
Must have
• Phrases:
- “Happy Labour Day”
- “20% off site wide sale*"
- "Coupon code: Harvest20"
- Underneath phrase the date of sale “September 3rd - 7th”
- In tiny print “*excludes all sale and bundled items”
- MUST BE 2000px x 600px
Nice to have
• - images of the products or bud we carry which can be found at www.fernlowleaf.com
- bold
Should not have
• - company logo
- the American flag, we are a Canadian company, colours and flag should all be Canadian

```html
<!DOCTYPE html>
<html lang="en">
<head>
<meta charset="utf-8">
<title>Happy Labour Day – 20% off site wide sale</title>
<link rel="stylesheet" href="https://fonts.googleapis.com/css2?family=Poppins:ital,wght@0,500;0,700;0,800;1,800&family=Kaushan+Script&display=swap">
<style>
  :root {
    --canvas-white: #ffffff;
    --soft-grey: #f1f1f1;
    --banner-red: #d30000;
    --banner-red-deep: #b80000;
    --banner-red-light: #e8130f;
    --text-white: #ffffff;
    --text-red: #d10000;
    --bunting-red: #e9464a;
    --bunting-pale: #f7d3d3;
  }
  * { margin: 0; padding: 0; box-sizing: border-box; }
  html, body { width: 1200px; height: 360px; overflow: hidden; background: var(--canvas-white); }
  .banner {
    position: relative;
    width: 1200px;
    height: 360px;
    overflow: hidden;
    background: var(--canvas-white);
    font-family: "Poppins", Arial, sans-serif;
    color: var(--text-white);
  }
  .banner__backdrop { position: absolute; inset: 0; width: 1200px; height: 360px; }
  .product {
    position: absolute;
    border-radius: 6px;
  }
  .product--cartridges { left: 51px; top: 78px; width: 84px; height: 135px;
    background: linear-gradient(180deg, #2a2a2a, #11110d 60%, #8a7a2a); }
  .product--concentrate-bags { left: 196px; top: 42px; width: 134px; height: 168px;
    background: linear-gradient(135deg, #3a3f52, #7b6b8d 50%, #c9c0a4); }
  .product--jelly-bombs { left: 54px; top: 243px; width: 180px; height: 84px;
    background: linear-gradient(90deg, #ef7a1c, #e3c21a 35%, #4fae3a 65%, #d8325a); }
  .product--sanitizer-holders { left: 283px; top: 184px; width: 98px; height: 149px;
    border-radius: 14px;
    background: linear-gradient(90deg, #3bb3b8, #f2d23a 50%, #3a8fd9); }

  .headline { position: absolute; left: 416px; top: 118px; }
  .headline__happy {
    display: block;
    margin-left: 152px;
    font-family: "Kaushan Script", cursive;
    font-size: 40px;
    line-height: 1;
  }
  .headline__title {
    display: block;
    margin-top: -2px;
    font-weight: 800;
    font-size: 70px;
    line-height: 1;
    letter-spacing: -0.5px;
  }
  .offer {
    position: absolute;
    right: 48px;
    top: 80px;
    text-align: right;
  }
  .offer__discount {
    display: block;
    font-weight: 800;
    font-style: italic;
    font-size: 47px;
    line-height: 1.05;
    letter-spacing: -1px;
  }
  .offer__scope {
    display: block;
    font-weight: 500;
    font-size: 24px;
    line-height: 1.1;
  }
  .coupon {
    position: absolute;
    left: 877px;
    top: 193px;
    width: 282px;
    height: 38px;
    border-radius: 19px;
    background: var(--canvas-white);
    color: var(--text-red);
    font-weight: 500;
    font-size: 21px;
    line-height: 38px;
    text-align: center;
    white-space: nowrap;
  }
  .coupon__code { font-weight: 700; }
  .sale-dates {
    position: absolute;
    right: 48px;
    top: 255px;
    font-weight: 700;
    font-size: 21px;
    line-height: 1.2;
  }
  .fine-print {
    position: absolute;
    right: 48px;
    top: 306px;
    font-weight: 500;
    font-size: 18.5px;
    line-height: 1.2;
  }
</style>
</head>
<body>
<main class="banner">
  <svg class="banner__backdrop" viewBox="0 0 1200 360" aria-hidden="true">
    <defs>
      <linearGradient id="redPanel" x1="0" y1="0" x2="1" y2="1">
        <stop offset="0" stop-color="var(--banner-red-light)"/>
        <stop offset="0.6" stop-color="var(--banner-red)"/>
        <stop offset="1" stop-color="var(--banner-red-deep)"/>
      </linearGradient>
      <linearGradient id="buntingTone" x1="0" y1="0" x2="1" y2="0">
        <stop offset="0" stop-color="var(--bunting-pale)"/>
        <stop offset="0.5" stop-color="var(--bunting-red)"/>
        <stop offset="1" stop-color="var(--bunting-pale)"/>
      </linearGradient>
    </defs>
    <rect width="1200" height="360" fill="var(--canvas-white)"/>
    <path d="M388,0 C378,120 410,270 480,360 L1200,360 L1200,0 Z" fill="url(#redPanel)"/>
  </svg>

  <svg class="banner__bunting" viewBox="0 0 1200 360" width="1200" height="360"
       style="position:absolute;inset:0" role="img"
       aria-label="Strings of red and white bunting flags with maple leaves">
    <path d="M0,60 Q80,45 150,0 L150,14 Q90,62 0,80 Z" fill="url(#buntingTone)" opacity="0.8"/>
    <path d="M350,0 Q600,90 880,0 L870,30 Q600,115 360,30 Z" fill="url(#buntingTone)" opacity="0.85"/>
    <path d="M1045,0 Q1110,55 1200,70 L1200,88 Q1100,75 1035,15 Z" fill="url(#buntingTone)" opacity="0.85"/>
  </svg>

  <div class="product product--cartridges" role="img" aria-label="Photo of vape cartridges in black tubes"></div>
  <div class="product product--concentrate-bags" role="img" aria-label="Photo of a fanned stack of concentrate packages"></div>
  <div class="product product--jelly-bombs" role="img" aria-label="Photo of fruit jelly edibles in orange, mango, apple and cherry packs"></div>
  <div class="product product--sanitizer-holders" role="img" aria-label="Photo of hand sanitizer bottles in silicone holders on a hook"></div>

  <h1 class="headline">
    <span class="headline__happy">Happy</span>
    <span class="headline__title">Labour Day</span>
  </h1>

  <p class="offer">
    <span class="offer__discount">20% off</span>
    <span class="offer__scope">site wide sale</span>
  </p>

  <p class="coupon">Coupon Code: <span class="coupon__code">Harvest20</span></p>

  <p class="sale-dates">September 3rd - 7th</p>

  <p class="fine-print">*excludes all sale and bundled items</p>
</main>
</body>
</html>
```